Minimalist- A clean spacious and crisp design for a Security Consulting Company

I need a design for a security consultant that deals with the upper end of town for security design, including CCTV and other electronic design. I need it to look spacious and be very simplistic in design. I want to keep it looking like Plonka or VANTU's website. I have experience in business intelligence. and have a lot of high end clients in the diamond industry and mining. My key area of income is consulting and taking them from normal to excellent security.
Target Market(s)
People interested in doing business with me
Industry/Entity Type
Electronic
Coding
Coded - Design and coding required
Number of Pages Required
4 page
Requirements
Must have
- The least amount of text possible
- A simple and nice front page with the logo.
- A contact us button
- Specialised projects button
- About us button
- Business intelligence button
Should not have
- Cluttered un-useful information

```html
<!DOCTYPE html>
<html lang="en">
<head>
<meta charset="utf-8">
<title>Norvane Strategy</title>
<link href="https://fonts.googleapis.com/css2?family=Lato:wght@400;700&family=Tinos:wght@400&display=swap" rel="stylesheet">
<style>
:root{
  --red:#9b0000;
  --red-bright:#b10f0f;
  --ink:#1c1c1c;
  --text:#555;
  --paper:#f4f4f4;
  --white:#fff;
  --dark:#2d2d2d;
  --darker:#1e1e1e;
  --rule:#cfcfcf;
}
*{box-sizing:border-box;margin:0;padding:0}
html,body{width:1200px;height:3564px;overflow:hidden}
body{font-family:'Lato',sans-serif;color:var(--text);background:var(--paper);position:relative}
section,header,footer{position:absolute;left:0;width:1200px}
.accent{color:var(--red)}

/* header */
.site-header{top:0;height:105px;background:var(--white)}
.brand{position:absolute;left:132px;top:24px;width:320px;height:60px}
.brand-mark{position:absolute;left:0;top:4px;width:40px;height:40px;background:var(--red)}
.brand-name{position:absolute;left:52px;top:2px;font-family:'Tinos',serif;font-size:30px;color:var(--ink);line-height:34px;white-space:nowrap}
.brand-tag{position:absolute;left:53px;top:36px;font-size:13px;color:#888;white-space:nowrap}
.main-nav{position:absolute;right:112px;top:0;height:105px;display:flex}
.main-nav a{display:flex;align-items:center;padding:0 20px;font-family:'Tinos',serif;font-size:18px;color:#444;text-decoration:none;border-left:1px solid #e2e2e2;height:50px;margin-top:28px}
.main-nav a:first-child{border:0}
.main-nav a.active{background:var(--red);color:var(--white);height:105px;margin-top:0;padding:0 24px}

/* hero */
.hero{top:105px;height:518px;overflow:hidden}
.hero-visual{position:absolute;inset:0;background:radial-gradient(ellipse at 60% 40%,#3a5c78 0%,#1a2c3e 45%,#0b1420 100%)}
.hero-band{position:absolute;left:0;top:313px;width:620px;height:133px;background:rgba(255,255,255,.82)}
.hero-title{position:absolute;left:135px;top:336px;font-size:37px;line-height:44px;color:#222;font-weight:400}
.hero-title strong{color:var(--red);font-weight:700}
.hero-dots{position:absolute;left:570px;top:486px;display:flex;gap:9px}
.hero-dots span{width:9px;height:9px;border-radius:50%;background:rgba(255,255,255,.5)}
.hero-dots span:first-child{background:var(--red-bright)}

/* shared titles */
.section-title{position:absolute;left:0;width:1200px;text-align:center;font-family:'Tinos',serif;font-size:42px;line-height:48px;color:var(--ink);font-weight:400}
.divider{position:absolute;left:380px;width:440px;height:1px;background:var(--rule)}
.divider-dot{position:absolute;left:587px;width:26px;height:26px;border-radius:50%;background:#777;border:4px solid var(--paper)}
.lead{position:absolute;left:140px;width:920px;text-align:center;font-size:14px;line-height:24px}
.lead a{color:var(--red)}

.welcome{top:623px;height:282px}

/* services */
.services{top:905px;height:527px;background:var(--red);color:#f3dede}
.services .divider{background:rgba(255,255,255,.25)}
.services .divider-dot{border-color:var(--red);background:#ddd}
.service{position:absolute;top:212px;width:300px}
.service-icon{position:absolute;left:0;top:0;width:74px;height:74px;border-radius:50%}
.service h3{position:absolute;left:86px;top:2px;font-family:'Tinos',serif;font-weight:400;font-size:25px;line-height:28px;color:var(--white)}
.service p{position:absolute;left:86px;width:210px;font-size:14px;line-height:24px;color:#f6e3e3}
.plus-box{position:absolute;width:20px;height:20px;background:#2a0000;color:#fff;font-size:16px;line-height:19px;text-align:center}
.slide-arrow{position:absolute;top:285px;width:34px;height:68px;background:rgba(0,0,0,.2)}
.slide-arrow svg{position:absolute;top:24px;left:10px}

/* industries */
.industries{top:1432px;height:638px}
.industry{position:absolute;width:300px}
.industry h3{font-family:'Tinos',serif;font-weight:400;font-size:25px;color:var(--ink)}
.industry p{font-size:14px;line-height:24px;margin-top:6px}
.industry.left{text-align:right}
.industry-icon{position:absolute;width:78px;height:78px;border-radius:6px}
.hub{position:absolute;left:550px;top:276px;width:100px;height:100px;border-radius:50%;background:radial-gradient(circle at 35% 35%,#fff,#b9b9b9)}
.plus-grey{position:absolute;width:20px;height:20px;background:#666;color:#fff;font-size:16px;line-height:19px;text-align:center}

/* vision */
.values{top:2070px;height:398px;overflow:hidden}
.values-visual{position:absolute;inset:0;background:linear-gradient(135deg,#102338 0%,#1f3d5c 45%,#0a1622 100%)}
.value-col{position:absolute;top:55px;width:300px;height:300px;text-align:center;color:#e6ecf2}
.value-col.panel{background:rgba(255,255,255,.08)}
.value-col h3{font-family:'Tinos',serif;font-weight:400;font-size:40px;color:var(--white);margin-top:24px}
.value-col p{font-size:14px;line-height:24px;width:230px;margin:18px auto 0}

/* process */
.process{top:2468px;height:502px}
.tabs{position:absolute;left:134px;top:164px;width:932px;height:2px;background:var(--rule)}
.tab{position:absolute;top:164px;width:190px;text-align:center;font-family:'Tinos',serif;font-size:25px;color:#555;padding-top:18px}
.tab::before{content:"";position:absolute;left:40px;top:0;width:110px;height:3px;background:#444}
.tab.active{color:var(--red)}
.tab.active::before{background:var(--red);left:0;width:190px}
.process-visual{position:absolute;left:178px;top:262px;width:130px;height:160px;background:linear-gradient(#a51717,#8a0000);border-radius:10px}
.process-text{position:absolute;left:392px;top:280px;width:680px;font-size:14px;line-height:24px}

/* footer */
.contact{top:2970px;height:540px;background:var(--dark);color:#cfcfcf}
.mail-badge{position:absolute;left:567px;top:23px;width:66px;height:66px;border-radius:50%;background:#fff}
.mail-badge svg{position:absolute;left:19px;top:22px}
.contact h2{position:absolute;top:118px;left:0;width:1200px;text-align:center;font-family:'Tinos',serif;font-weight:400;font-size:25px;color:#fff}
.contact .intro{position:absolute;top:155px;left:0;width:1200px;text-align:center;font-size:14px;line-height:20px}
.contact .divider{top:203px;background:#555}
.col-title{position:absolute;top:250px;font-size:21px;color:#ddd}
.field{position:absolute;left:132px;width:300px;background:#1c1c1c;color:#999;font-size:12px;padding:7px 10px}
.send{position:absolute;left:132px;top:490px;width:104px;height:32px;background:linear-gradient(#f2f2f2,#bdbdbd);color:#222;font-weight:700;font-size:14px;text-align:center;line-height:32px;border-radius:2px}
.map{position:absolute;left:488px;top:288px;width:321px;height:192px;background:linear-gradient(135deg,#e8e4d8,#cfd9c6 60%,#dfe5ee)}
.find{position:absolute;left:860px;width:260px;font-size:14px;color:#ddd}
.find .row{position:absolute;left:0;display:flex;gap:12px;align-items:flex-start;width:260px}
.find .row span{line-height:18px}
.social{position:absolute;left:846px;top:460px;display:flex;gap:14px}
.social span{width:22px;height:22px;background:#d8d8d8;border-radius:2px}
.copyright{top:3510px;height:54px;background:var(--darker);color:#aaa;font-size:12px;text-align:center;line-height:54px}
</style>
</head>
<body>

<header class="site-header">
  <div class="brand">
    <span class="brand-mark"></span>
    <span class="brand-name">Norvane Strategy</span>
    <span class="brand-tag">Creative Solutions</span>
  </div>
  <nav class="main-nav">
    <a class="active" href="#">Home</a>
    <a href="#">About Us</a>
    <a href="#">Services</a>
    <a href="#">Products</a>
    <a href="#">Industries</a>
    <a href="#">Contact Us</a>
  </nav>
</header>

<section class="hero">
  <div class="hero-visual" role="img" aria-label="Hand touching a glowing cube above a blue circuit board"></div>
  <div class="hero-band"></div>
  <h1 class="hero-title">We <strong>build the difference</strong><br>and they will <strong>want it.</strong></h1>
  <div class="hero-dots"><span></span><span></span><span></span></div>
</section>

<section class="welcome">
  <h2 class="section-title" style="top:42px">Welcome to Norvane<span class="accent">Strategy</span></h2>
  <div class="divider" style="top:105px"></div>
  <div class="divider-dot" style="top:92px"></div>
  <p class="lead" style="top:140px">Sed ut perspiciatis unde omnis iste natus error sit voluptatem accusantium doloremque laudantium, totam rem aperiam, eaque ipsa quae ab illo inventore veritatis et quasi architecto beatae vitae dicta sunt explicabo. Nemo enim ipsam voluptatem quia voluptas sit aspernatur aut odit aut voluptas sit aspernatur aut odit aut fugit. <a href="#">More</a></p>
</section>

<section class="services">
  <h2 class="section-title" style="top:36px">Professional <span style="color:#fff">Services</span></h2>
  <div class="divider" style="top:100px"></div>
  <div class="divider-dot" style="top:87px"></div>
  <p class="lead" style="top:140px;color:#f3dede">Sed ut perspiciatis unde omnis iste natus error sit voluptatem accusantium doloremque laudantium, totam rem aperiam</p>

  <div class="slide-arrow" style="left:62px;border-radius:0 34px 34px 0"><svg width="12" height="20"><path d="M10 2 2 10l8 8" stroke="#fff" stroke-width="3" fill="none"/></svg></div>
  <div class="slide-arrow" style="right:62px;border-radius:34px 0 0 34px"><svg width="12" height="20"><path d="M2 2l8 8-8 8" stroke="#fff" stroke-width="3" fill="none"/></svg></div>

  <div class="service" style="left:138px">
    <div class="service-icon" style="background:#f3c21b"></div>
    <h3>Consulting</h3>
    <p style="top:34px">Sed ut perspiciatis unde omnis iste natus error sit voluptatem accusantium doloremque lau dantium, totam rem aper iam, eaque ipsa quae ab illo inve ntore veritatis et quasi arch itecto beatae vitae dicta sunt explicabo.</p>
    <div class="plus-box" style="left:86px;top:258px">+</div>
  </div>
  <div class="service" style="left:460px">
    <div class="service-icon" style="background:#f26a24"></div>
    <h3>Business<br>Intelligence</h3>
    <p style="top:62px">Sed ut perspiciatis unde omnis iste natus error sit voluptatem accusantium doloremque lau dantium, totam rem aper iam, eaque ipsa quae ab illo inve ntore veritatis et quasi arch itecto beatae vitae dicta sunt explicabo.</p>
    <div class="plus-box" style="left:86px;top:258px">+</div>
  </div>
  <div class="service" style="left:782px">
    <div class="service-icon" style="background:#2d8fd8"></div>
    <h3>Security design</h3>
    <p style="top:34px">Sed ut perspiciatis unde omnis iste natus error sit voluptatem accusantium doloremque lau dantium, totam rem aper iam, eaque ipsa quae ab illo inve ntore veritatis et quasi arch itecto beatae vitae dicta sunt explicabo.</p>
    <div class="plus-box" style="left:86px;top:258px">+</div>
  </div>
</section>

<section class="industries">
  <h2 class="section-title" style="top:42px">Industries <span class="accent">We Serve</span></h2>
  <div class="divider" style="top:105px"></div>
  <div class="divider-dot" style="top:92px"></div>

  <svg style="position:absolute;left:510px;top:190px" width="180" height="280" viewBox="0 0 180 280" fill="none" stroke="#333" stroke-width="2.5">
    <path d="M50 70 C30 40 15 30 5 28"/><path d="M5 28 l14 -6 M5 28 l10 11"/>
    <path d="M130 70 C150 40 165 30 175 28"/><path d="M175 28 l-14 -6 M175 28 l-10 11"/>
    <path d="M50 210 C30 240 15 250 5 252"/><path d="M5 252 l14 6 M5 252 l10 -11"/>
    <path d="M130 210 C150 240 165 250 175 252"/><path d="M175 252 l-14 6 M175 252 l-10 -11"/>
  </svg>
  <div class="hub"></div>

  <div class="industry-icon" style="left:408px;top:168px;background:#f0a52a" role="img" aria-label="Government building icon"></div>
  <div class="industry left" style="left:92px;top:170px">
    <h3>Government</h3>
    <p>Sed ut perspiciatis unde omnis iste natus error sit voluptatem accusantium doloremque lau dantium, totam rem aper iam</p>
  </div>
  <div class="plus-grey" style="left:370px;top:320px">+</div>

  <div class="industry-icon" style="left:738px;top:168px;background:#4d8fd3" role="img" aria-label="Commercial office tower icon"></div>
  <div class="industry" style="left:818px;top:170px">
    <h3>Commercial</h3>
    <p>Sed ut perspiciatis unde omnis iste natus error sit voluptatem accusantium doloremque lau dantium, totam rem aper iam</p>
  </div>
  <div class="plus-grey" style="left:818px;top:320px">+</div>

  <div class="industry-icon" style="left:408px;top:410px;background:#e9a33a" role="img" aria-label="Construction crane icon"></div>
  <div class="industry left" style="left:92px;top:412px">
    <h3>Construction</h3>
    <p>Sed ut perspiciatis unde omnis iste natus error sit voluptatem accusantium doloremque lau dantium, totam rem aper iam</p>
  </div>
  <div class="plus-grey" style="left:370px;top:562px">+</div>

  <div class="industry-icon" style="left:730px;top:410px;background:#e5532f" role="img" aria-label="Heart with pulse line icon"></div>
  <div class="industry" style="left:818px;top:412px">
    <h3>Health</h3>
    <p>Sed ut perspiciatis unde omnis iste natus error sit voluptatem accusantium doloremque lau dantium,</p>
  </div>
  <div class="plus-grey" style="left:818px;top:562px">+</div>
</section>

<section class="values">
  <div class="values-visual" role="img" aria-label="Dark blue technology backdrop with a padlock and globe"></div>
  <div class="value-col" style="left:126px">
    <h3>Vision</h3>
    <p>We, a united Norvane Strategy team, are committed to growing our people and refining our processes to produce a minimum of 10% increase in our profit per quarter in 2014. In addition, we are focussed on building our Client base by one new Client per quarter, in 2014.</p>
  </div>
  <div class="value-col panel" style="left:450px">
    <h3>Mission</h3>
    <p>As a Team we are committed to building mutual respect between each member and our Clients. Based on mutual respect we will develop mutually rewarding relationships between our team members and our Clients.</p>
  </div>
  <div class="value-col panel" style="left:776px">
    <h3>Values</h3>
    <p>At the core of our values are our people, who are committed to developing partnerships between Norvane Strategy and our Clients through constant and consistent communication.</p>
  </div>
</section>

<section class="process">
  <h2 class="section-title" style="top:56px">Business <span class="accent">Process</span></h2>
  <div class="divider" style="top:116px;left:345px;width:510px"></div>
  <div class="tabs"></div>
  <div class="tab active" style="left:134px">Consulting</div>
  <div class="tab" style="left:390px">Estimates</div>
  <div class="tab" style="left:616px">Proposals</div>
  <div class="tab" style="left:842px">Projects</div>
  <div class="process-visual" role="img" aria-label="Red icon of two people meeting at a table"></div>
  <p class="process-text">Sed ut perspiciatis unde omnis iste natus error sit voluptatem accusantium doloremque lau dantium, totam rem aper iam, eaque ipsa quae ab illo inve ntore veritatis et quasi arch itecto beatae vitae dicta sunt explicabo.&nbsp; Sed ut perspiciatis unde omnis iste natus error sit voluptatem accusantium doloremque lau dantium, totam rem aper iam, eaque ipsa quae ab illo inve ntore veritatis et quasi arch itecto beatae vitae dicta sunt explicabo.</p>
</section>

<footer class="contact">
  <div class="mail-badge"><svg width="28" height="22" viewBox="0 0 28 22"><rect x="1" y="1" width="26" height="20" fill="#333"/><path d="M1 1l13 11L27 1" stroke="#fff" stroke-width="2" fill="none"/></svg></div>
  <h2>Contact Us</h2>
  <p class="intro">Please, Feel free to contact anytime. it's always<br>a pleasure meeting new people.</p>
  <div class="divider"></div>

  <div class="col-title" style="left:140px">Drop us a line</div>
  <div class="field" style="top:288px;height:28px">Name</div>
  <div class="field" style="top:324px;height:28px">Email</div>
  <div class="field" style="top:360px;height:116px">Message</div>
  <div class="send">SEND</div>

  <div class="col-title" style="left:488px">Location Map</div>
  <div class="map" role="img" aria-label="Road map showing the office location"></div>

  <div class="col-title" style="left:860px">Find Us</div>
  <div class="find" style="top:290px">
    <div class="row" style="top:0;left:-14px"><svg width="12" height="16" viewBox="0 0 12 16"><path d="M6 0a6 6 0 0 1 6 6c0 4-6 10-6 10S0 10 0 6a6 6 0 0 1 6-6z" fill="#ddd"/><circle cx="6" cy="6" r="2" fill="#2d2d2d"/></svg><span style="font-size:12px">123 euismod cidun ut laoreet<br>laoreet dol magna aliquam<br>PG Feugait</span></div>
    <div class="row" style="top:74px;left:-14px"><svg width="14" height="14" viewBox="0 0 14 14"><path d="M3 0l3 3-2 2c1 2 3 4 5 5l2-2 3 3-2 3C6 14 0 8 0 3z" fill="#ddd"/></svg><span style="font-weight:700">(555) 014 - 2290</span></div>
    <div class="row" style="top:106px;left:-14px"><svg width="14" height="14" viewBox="0 0 14 14"><rect x="1" y="4" width="12" height="9" fill="#ddd"/><rect x="3" y="0" width="8" height="5" fill="#ddd"/></svg><span style="font-weight:700">(555) 014 - 2290</span></div>
    <div class="row" style="top:138px;left:-14px"><svg width="14" height="11" viewBox="0 0 14 11"><rect width="14" height="11" fill="#ddd"/><path d="M0 0l7 6 7-6" stroke="#2d2d2d" fill="none"/></svg><span style="font-size:13px">hello@norvanestrategy.com</span></div>
  </div>
  <div class="social"><span></span><span></span><span></span><span></span></div>
</footer>

<footer class="copyright">Copyright © 2015 Norvane Strategy . All Right Reserved</footer>

</body>
</html>
```